MD Trailcraft & Wildland Fair

I need a 1 page flyer for promotion of an upcoming sportsman and outdoor show(expo). would like the flyer to be able to be printed in B&W and color! show will include all things to do with the out doors, hunting fishing boating hiking atv camping rvs motorcycles. the event will have a kids zone, events games and activities for kids. there will be vendors showing the newest products. guest speakers and industry experts giving training and advice. this show will have something for everyone. food trucks and concessions. 200+ vendors. waterfould calling competition. deer/buck scoring casting competition for kids 3D Archery competitions

Target Market(s)

anyone event open to all ages!

Colors
ec1f27
000000
fbed22

Requirements
Must have
• date- september 1-2 2018
• location Pelling valley expo 4837 orchardmill rd east calverton MD 21652
• facebook - mdtrailcraftfair
• email mdtrailcraftfair@quorvex.com
• web www.mdtrailcraftfair.com
• vendor spaces still available! sign up now space going fast
Nice to have
• would like some thing that can be both printed in B&W and Color, and still have a great affect.
Should not have
• open to any suggestions

```html
<!DOCTYPE html>
<html lang="en">
<head>
<meta charset="utf-8">
<title>MD Trailcraft &amp; Wildland Fair – Vendor Flyer</title>
<link href="https://fonts.googleapis.com/css2?family=Cinzel:wght@400;600;700&family=Lato:ital,wght@0,400;0,700;0,900;1,700;1,900&display=swap" rel="stylesheet">
<style>
  :root {
    --red: #ec1f27;
    --red-dark: #c8141c;
    --black: #000000;
    --ink: #111111;
    --white: #ffffff;
    --stage: #e1e1e1;
    --panel-light: #ffffff;
    --panel-grey: #d6d6d6;
    --tent-sky: #c9dcea;
    --tent-grass: #7e9a45;
    --tent-blue: #3d7fc4;
    --sand: #d9c39a;
    --archer-orange: #e4762b;
    --fairway: #5d8f2c;
    --water: #8fcde0;
  }
  * { box-sizing: border-box; margin: 0; padding: 0; }
  html, body { width: 1200px; height: 1200px; overflow: hidden; }
  body { background: var(--stage); font-family: "Lato", sans-serif; color: var(--ink); }

  .flyer {
    position: absolute; left: 207px; top: 93px;
    width: 787px; height: 1016px; background: var(--white); overflow: hidden;
  }
  .block { position: absolute; }

  .title-box {
    left: 0; top: 0; width: 383px; height: 120px; background: var(--red);
    display: flex; align-items: center; justify-content: center; text-align: center;
    font-family: "Cinzel", serif; font-weight: 700; color: var(--white);
    font-size: 33px; line-height: 41px;
  }
  .date-box {
    left: 0; top: 423px; width: 272px; height: 133px;
    background: linear-gradient(135deg, var(--red-dark), var(--red));
    display: flex; flex-direction: column; align-items: center; justify-content: center;
    font-family: "Cinzel", serif; font-weight: 600; color: var(--white); line-height: 1.08;
  }
  .date-box .month { font-size: 37px; }
  .date-box .days { font-size: 44px; }

  .photo { overflow: hidden; }
  .photo-tents { left: 0; top: 126px; width: 383px; height: 164px;
    background: linear-gradient(180deg, var(--tent-sky) 0%, #8fa96a 30%, var(--tent-grass) 55%, #6f8f3a 100%); }
  .photo-archery { left: 390px; top: 0; width: 397px; height: 290px;
    background: linear-gradient(100deg, var(--archer-orange) 0%, #c48a52 38%, var(--sand) 62%, #cfb585 100%); }
  .photo-golf { left: 0; top: 295px; width: 272px; height: 124px;
    background: linear-gradient(120deg, #9cc25a 0%, var(--fairway) 55%, #3e6a1e 100%); }
  .photo-jetski { left: 279px; top: 295px; width: 508px; height: 261px;
    background: linear-gradient(160deg, #6fb3c9 0%, var(--water) 40%, #d9eef4 70%, #a8d8e6 100%); }

  .info {
    left: 0; top: 556px; width: 787px; height: 394px;
    background: linear-gradient(180deg, var(--panel-grey) 0%, var(--panel-light) 45%, var(--panel-grey) 100%);
  }
  .headline {
    position: absolute; top: 20px; left: 0; width: 100%; text-align: center;
    font-weight: 900; font-size: 26px; line-height: 31px; letter-spacing: -0.3px;
  }
  .offer-list { position: absolute; top: 103px; list-style: none; }
  .offer-list li {
    font-size: 16px; line-height: 24px; font-weight: 400; padding-left: 17px; position: relative;
  }
  .offer-list li svg { position: absolute; left: 0; top: 8px; width: 10px; height: 10px; }
  .col-1 { left: 25px; } .col-2 { left: 239px; } .col-3 { left: 420px; } .col-4 { left: 598px; }

  .divider { position: absolute; left: 153px; top: 277px; width: 449px; height: 2px; background: var(--red); }
  .pitch {
    position: absolute; top: 290px; left: 40px; width: 707px; text-align: center;
    font-family: "Cinzel", serif; font-weight: 600; font-size: 19.5px; line-height: 21px; letter-spacing: 0.5px;
  }
  .expect {
    position: absolute; top: 333px; left: 0; width: 100%; text-align: center;
    color: var(--red); font-style: italic; font-weight: 700; font-size: 15px;
  }
  .vendor-cta {
    position: absolute; top: 352px; left: 0; width: 100%; text-align: center;
    color: var(--red); font-style: italic; font-weight: 900; font-size: 19.7px; letter-spacing: -0.4px;
  }

  .footer {
    left: 0; top: 950px; width: 787px; height: 66px; background: var(--black); color: var(--white);
    display: flex; align-items: center; padding: 0 24px; font-size: 10.5px;
  }
  .contact { display: flex; align-items: center; gap: 10px; }
  .contact svg { flex: none; }
  .contact-address { width: 270px; line-height: 13px; }
  .contact-social { width: 136px; }
  .contact-email { width: 200px; }
  .social-mark { width: 14px; height: 14px; border-radius: 50%; background: var(--white); flex: none; }
</style>
</head>
<body>
  <main class="flyer">
    <h1 class="block title-box">MD TRAILCRAFT &amp;<br>WILDLAND FAIR</h1>

    <div class="block photo photo-tents" role="img" aria-label="Photo of colourful camping tents spread across a grassy field under trees"></div>
    <div class="block photo photo-archery" role="img" aria-label="Photo of an archer in an orange vest drawing a bow toward a target on sand"></div>
    <div class="block photo photo-golf" role="img" aria-label="Photo of a golf ball on a tee beside a club"></div>
    <div class="block photo photo-jetski" role="img" aria-label="Photo of a rider on a jet ski throwing up spray"></div>

    <div class="block date-box">
      <span class="month">SEPTEMBER</span>
      <span class="days">1-2, 2018</span>
    </div>

    <section class="block info">
      <h2 class="headline">Over 60,000 sqft of INDOOR and 30,000+ sqft<br>OUTDOOR products and services including:</h2>

      <ul class="offer-list col-1">
        <li><svg viewBox="0 0 10 10"><path d="M1 5.5 L4 8.5 L9 1.5" fill="none" stroke="#ec1f27" stroke-width="2"/></svg>Sports Equipment</li>
        <li><svg viewBox="0 0 10 10"><path d="M1 5.5 L4 8.5 L9 1.5" fill="none" stroke="#ec1f27" stroke-width="2"/></svg>Campers</li>
        <li><svg viewBox="0 0 10 10"><path d="M1 5.5 L4 8.5 L9 1.5" fill="none" stroke="#ec1f27" stroke-width="2"/></svg>Boats</li>
        <li><svg viewBox="0 0 10 10"><path d="M1 5.5 L4 8.5 L9 1.5" fill="none" stroke="#ec1f27" stroke-width="2"/></svg>RV’s</li>
        <li><svg viewBox="0 0 10 10"><path d="M1 5.5 L4 8.5 L9 1.5" fill="none" stroke="#ec1f27" stroke-width="2"/></svg>Tackle &amp; Bait</li>
        <li><svg viewBox="0 0 10 10"><path d="M1 5.5 L4 8.5 L9 1.5" fill="none" stroke="#ec1f27" stroke-width="2"/></svg>Motorcycles</li>
      </ul>
      <ul class="offer-list col-2">
        <li><svg viewBox="0 0 10 10"><path d="M1 5.5 L4 8.5 L9 1.5" fill="none" stroke="#ec1f27" stroke-width="2"/></svg>ATV’s</li>
        <li><svg viewBox="0 0 10 10"><path d="M1 5.5 L4 8.5 L9 1.5" fill="none" stroke="#ec1f27" stroke-width="2"/></svg>Trucks</li>
        <li><svg viewBox="0 0 10 10"><path d="M1 5.5 L4 8.5 L9 1.5" fill="none" stroke="#ec1f27" stroke-width="2"/></svg>Taxidermists</li>
        <li><svg viewBox="0 0 10 10"><path d="M1 5.5 L4 8.5 L9 1.5" fill="none" stroke="#ec1f27" stroke-width="2"/></svg>Outfitters</li>
        <li><svg viewBox="0 0 10 10"><path d="M1 5.5 L4 8.5 L9 1.5" fill="none" stroke="#ec1f27" stroke-width="2"/></svg>Guns</li>
        <li><svg viewBox="0 0 10 10"><path d="M1 5.5 L4 8.5 L9 1.5" fill="none" stroke="#ec1f27" stroke-width="2"/></svg>Jet Skis</li>
      </ul>
      <ul class="offer-list col-3">
        <li><svg viewBox="0 0 10 10"><path d="M1 5.5 L4 8.5 L9 1.5" fill="none" stroke="#ec1f27" stroke-width="2"/></svg>Charter Boats</li>
        <li><svg viewBox="0 0 10 10"><path d="M1 5.5 L4 8.5 L9 1.5" fill="none" stroke="#ec1f27" stroke-width="2"/></svg>Golf Resorts</li>
        <li><svg viewBox="0 0 10 10"><path d="M1 5.5 L4 8.5 L9 1.5" fill="none" stroke="#ec1f27" stroke-width="2"/></svg>Knives</li>
        <li><svg viewBox="0 0 10 10"><path d="M1 5.5 L4 8.5 L9 1.5" fill="none" stroke="#ec1f27" stroke-width="2"/></svg>Archery</li>
        <li><svg viewBox="0 0 10 10"><path d="M1 5.5 L4 8.5 L9 1.5" fill="none" stroke="#ec1f27" stroke-width="2"/></svg>Trailers</li>
        <li><svg viewBox="0 0 10 10"><path d="M1 5.5 L4 8.5 L9 1.5" fill="none" stroke="#ec1f27" stroke-width="2"/></svg>Sporting Clubs</li>
      </ul>
      <ul class="offer-list col-4">
        <li><svg viewBox="0 0 10 10"><path d="M1 5.5 L4 8.5 L9 1.5" fill="none" stroke="#ec1f27" stroke-width="2"/></svg>Game Calls</li>
        <li><svg viewBox="0 0 10 10"><path d="M1 5.5 L4 8.5 L9 1.5" fill="none" stroke="#ec1f27" stroke-width="2"/></svg>Outdoor Magazines</li>
        <li><svg viewBox="0 0 10 10"><path d="M1 5.5 L4 8.5 L9 1.5" fill="none" stroke="#ec1f27" stroke-width="2"/></svg>Camp Grounds</li>
        <li><svg viewBox="0 0 10 10"><path d="M1 5.5 L4 8.5 L9 1.5" fill="none" stroke="#ec1f27" stroke-width="2"/></svg>Camping Equipment</li>
        <li><svg viewBox="0 0 10 10"><path d="M1 5.5 L4 8.5 L9 1.5" fill="none" stroke="#ec1f27" stroke-width="2"/></svg>Hunting Supplies</li>
        <li><svg viewBox="0 0 10 10"><path d="M1 5.5 L4 8.5 L9 1.5" fill="none" stroke="#ec1f27" stroke-width="2"/></svg>and much more...</li>
      </ul>

      <div class="divider"></div>
      <p class="pitch">SELL YOUR PRODUCTS and SERVICES TO THOUSANDS OF PEOPLE IN ONE WEEKEND!!</p>
      <p class="expect">WE ARE EXPECTING 2 DAY ATTENDANCE TO TOP 15,000 PEOPLE!</p>
      <p class="vendor-cta">VENDOR SPACES STILL AVAILABLE! SIGN UP NOW SPACE GOING FAST</p>
    </section>

    <footer class="block footer">
      <div class="contact contact-address">
        <svg width="14" height="19" viewBox="0 0 14 19"><path d="M7 0 C3 0 0 3 0 7 C0 12 7 19 7 19 C7 19 14 12 14 7 C14 3 11 0 7 0 Z M7 4 A3 3 0 1 1 7 10 A3 3 0 1 1 7 4 Z" fill="#fff" fill-rule="evenodd"/></svg>
        <span>Pelling valley expo,<br>4837 orchardmill rd east calverton MD 21652</span>
      </div>
      <div class="contact contact-social">
        <span class="social-mark"></span>
        <span>mdtrailcraftfair</span>
      </div>
      <div class="contact contact-email">
        <svg width="20" height="14" viewBox="0 0 20 14"><rect x="0" y="0" width="20" height="14" fill="#fff"/><path d="M0.5 0.8 L10 8 L19.5 0.8" fill="none" stroke="#000" stroke-width="1.6"/></svg>
        <span>mdtrailcraftfair@quorvex.com</span>
      </div>
      <div class="contact contact-web">
        <svg width="16" height="16" viewBox="0 0 16 16" fill="none" stroke="#fff" stroke-width="1.3"><circle cx="8" cy="8" r="7"/><ellipse cx="8" cy="8" rx="3" ry="7"/><path d="M1 8 H15 M2.5 4.5 H13.5 M2.5 11.5 H13.5"/></svg>
        <span>mdtrailcraftfair.com</span>
      </div>
    </footer>
  </main>
</body>
</html>
```